Landing Page for a Social Survey

Hi guys,
we need an elegant landing page for a new project. It's a social survey where users need to answer some questions to participate at a lottery.
I attached an example about what we want. As in the example the design should be very elegant and engage to user to click on the button and take part in the survey.
Also the design should look a bit like gathervine.
If you have any questions, don't hesitate to ask. I'll try to respond as soon as possible.
Please use the following texts:
Header: "Social Network Umfrage"
Headline above the text: "Herzlichen Glückwunsch"
Text:
"Sie wurden als einer von wenigen Nutzern aus Berlin und Umgebung ausgewählt an unserer Umfrage über Social Networks teilzunehmen.
Die Beantwortung der Fragen dauert nur wenige Sekunden. Als Dankeschön für Ihre Teilnahme können Sie ein Velor4, Orbo2 oder Quillnote Flux gewinnen."
Button: "Jetzt teilnehmen"

```html
<!DOCTYPE html>
<html lang="de">
<head>
<meta charset="utf-8">
<title>Social Network Umfrage</title>
<link href="https://fonts.googleapis.com/css2?family=Source+Sans+3:wght@400;600&display=swap" rel="stylesheet">
<style>
  :root {
    --header-blue: #76b3c7;
    --accent-blue: #6cadc2;
    --button-fill: #a9d2de;
    --button-border: #1f2a3a;
    --button-text: #5b8fa2;
    --panel-fill: #efefef;
    --panel-border: #b3b3b3;
    --card-white: #ffffff;
    --bg-top: #ffffff;
    --bg-bottom: #d2d6df;
    --white: #ffffff;
  }
  * { margin: 0; padding: 0; box-sizing: border-box; }
  html, body {
    width: 1200px;
    height: 900px;
    overflow: hidden;
  }
  body {
    position: relative;
    font-family: "Source Sans 3", "Myriad Pro", Arial, sans-serif;
    background: linear-gradient(to bottom, var(--bg-top) 81px, var(--bg-top) 140px, #e4e6ec 420px, var(--bg-bottom) 900px);
  }
  .site-header {
    position: absolute;
    left: 0; top: 0;
    width: 1200px; height: 81px;
    background: var(--header-blue);
    color: var(--white);
  }
  .site-title {
    position: absolute;
    left: 49px; top: 26px;
    font-size: 23px;
    font-weight: 400;
  }
  .site-date {
    position: absolute;
    right: 68px; top: 30px;
    font-size: 17px;
    letter-spacing: 3px;
  }
  .survey-card {
    position: absolute;
    left: 281px; top: 141px;
    width: 649px; height: 403px;
    background: var(--card-white);
    border-radius: 22px;
    box-shadow: 4px 6px 12px rgba(0, 0, 0, 0.35);
  }
  .survey-panel {
    position: absolute;
    left: 13px; top: 15px;
    width: 623px; height: 373px;
    background: var(--panel-fill);
    border: 1.5px solid var(--panel-border);
    border-radius: 11px;
  }
  .survey-headline {
    margin-top: 26px;
    text-align: center;
    font-size: 36px;
    font-weight: 400;
    color: var(--accent-blue);
  }
  .survey-text {
    margin: 20px 0 0 28px;
    width: 540px;
    font-size: 14px;
    line-height: 17px;
    letter-spacing: 1.9px;
    color: var(--accent-blue);
  }
  .survey-button {
    position: absolute;
    left: 209px; top: 255px;
    width: 204px; height: 49px;
    background: var(--button-fill);
    border: 3px solid var(--button-border);
    color: var(--button-text);
    font-family: "Source Sans 3", "Myriad Pro", Arial, sans-serif;
    font-size: 20px;
    display: flex;
    align-items: center;
    justify-content: center;
    box-shadow: inset 0 0 0 2px #c8e3ea;
    cursor: pointer;
  }
  .site-footer {
    position: absolute;
    left: 0; top: 851px;
    width: 1200px;
    text-align: center;
    font-size: 19px;
    color: var(--white);
  }
</style>
</head>
<body>
  <header class="site-header">
    <h1 class="site-title">Social Network Umfrage</h1>
    <div class="site-date">Jul 02, 2011</div>
  </header>

  <main class="survey-card">
    <section class="survey-panel">
      <h2 class="survey-headline">Herzlichen Glückwunsch!</h2>
      <p class="survey-text">Sie wurden als einer von wenigen Nutzern aus Berlin und Umgebung ausgewählt an unserer Umfrage über Social Networks teilzunehmen. Die Beantwortung der Fragen dauert nur wenige Sekunden. Als Dankeschön für Ihre Teilnahme können Sie ein Velor4, Orbo2 oder Quillnote Flux gewinnen.</p>
      <button class="survey-button" type="button">Jetzt teilnehmen</button>
    </section>
  </main>

  <footer class="site-footer">2011 All Rights Reserved</footer>
</body>
</html>
```